Business Card Design

We need a business card design for a Non-Profit Christian Based Organization located in Milford, Pa.
Alder Ridge Helping Harbor
Is a Christ-centered organization dedicated to providing compassion and hope to homeless or near homeless, families and individuals, by meeting their basic and urgent need of food, clothing and shelter.
Updates
the logo is black and white
and must add the color green some where 00400
Industry/Entity Type
Clothing
Contact Information for Business Card
Alder Ridge Helping Harbor
P.O. Box 287
Fernbrook, Pa 18990
Phone: (570) 413-CARE(2273)
Toll Free: (855) 413-CARE
email:Info@alderridgehh.org
email:Careline@alderridgehh.org
Our organization already has a logo.
Front of card:
Is a Christ-centered organization dedicated to providing compassion and hope to homeless or near homes, families and individual by meeting their basic and urgent need of food, clothing and shelter.(this is our Mission Statement)
On back of card:
'I was hungry and you gave me something to eat;
"I was thirsty and you gave me something to drink;
"I was a stranger and you invited me in."
Matthew 25:35
Color: Logo is black and white
Background color I would like a bright light green 00ff00(close to that)
I attached a sample of what I created on Quill Press but, I don't like the color green, nor the design (but I just wanted to give you and Idea of the Logo and Alder Ridge (one line) Helping Harbor (second line) in a different font thank you
Delia Rostova
Pr/Board of Directors

```html
<!DOCTYPE html>
<html lang="en">
<head>
<meta charset="utf-8">
<title>Alder Ridge Helping Harbor – Business Cards</title>
<link rel="stylesheet" href="https://fonts.googleapis.com/css2?family=Jost:wght@400;500&family=Quicksand:wght@300;400;500&family=Josefin+Sans:wght@400&display=swap">
<style>
  :root{
    --green:#66ff00;
    --lime:#a6ff00;
    --paper:#ededed;
    --ink:#111;
    --white:#fff;
    --label:#8ae600;
    --mission:#1f3a0a;
    --head-font:"Jost",sans-serif;
    --body-font:"Quicksand",sans-serif;
    --caps-font:"Josefin Sans",sans-serif;
  }
  *{margin:0;padding:0;box-sizing:border-box}
  html,body{width:1085px;height:1200px;overflow:hidden;background:var(--white)}
  .canvas{position:relative;width:1085px;height:1200px}
  .card-art{position:absolute;left:0;top:0}
  .t{position:absolute;white-space:nowrap}
  .logo-box{position:absolute;background:var(--white)}

  /* front card */
  .contact-label{font-family:var(--body-font);font-size:21px;letter-spacing:3px;color:var(--label);font-weight:400}
  .contact-value{font-family:var(--body-font);font-size:21px;letter-spacing:3px;color:var(--ink);font-weight:400}
  .org-name{font-family:var(--head-font);font-size:36px;letter-spacing:7px;color:var(--ink);font-weight:500}
  .org-tagline{font-family:var(--head-font);font-variant:small-caps;font-size:30px;letter-spacing:1px;color:var(--white)}
  .mission{position:absolute;left:55px;width:978px;top:510px;text-align:center;font-family:var(--body-font);font-weight:400;font-size:17px;line-height:25px;letter-spacing:.6px;color:var(--mission)}

  /* back card */
  .verse{font-family:var(--body-font);font-size:28px;color:var(--white);line-height:45px;font-weight:400}
  .foot-label{font-family:var(--caps-font);font-variant:small-caps;font-size:21px;letter-spacing:1px;color:var(--ink)}
  .foot-value{font-family:var(--body-font);font-size:22px;color:var(--label);font-weight:400}
  .foot-mail-label{font-family:var(--caps-font);font-variant:small-caps;font-size:19px;letter-spacing:2px;color:var(--label)}
  .foot-mail{font-family:var(--caps-font);font-variant:small-caps;font-size:21px;letter-spacing:1.5px;color:var(--ink)}
</style>
</head>
<body>
<main class="canvas">
  <svg class="card-art" width="1085" height="1200" viewBox="0 0 1085 1200" aria-hidden="true">
    <rect x="52" y="50" width="381" height="22" fill="var(--green)"/>
    <rect x="433" y="50" width="600" height="22" fill="var(--lime)"/>
    <rect x="50" y="72" width="983" height="293" fill="var(--paper)"/>
    <polygon points="50,72 435,72 263,365 50,365" fill="var(--lime)"/>
    <rect x="55" y="362" width="207" height="21" fill="var(--green)"/>
    <rect x="262" y="362" width="771" height="21" fill="var(--lime)"/>
    <rect x="53" y="383" width="980" height="200" fill="var(--green)"/>
    <rect x="55" y="625" width="562" height="22" fill="var(--lime)"/>
    <rect x="617" y="625" width="418" height="22" fill="var(--green)"/>
    <rect x="55" y="647" width="983" height="363" fill="var(--lime)"/>
    <path d="M55 647 H615 C560 660 530 720 535 790 C540 860 470 950 388 1010 H55 Z" fill="var(--green)"/>
    <rect x="55" y="1010" width="980" height="125" fill="var(--paper)"/>
    <rect x="55" y="1135" width="330" height="23" fill="var(--lime)"/>
    <rect x="385" y="1135" width="650" height="23" fill="var(--green)"/>
  </svg>

  <!-- front card content -->
  <div class="logo-box" style="left:121px;top:95px;width:105px;height:138px"></div>

  <span class="t contact-label" style="left:482px;top:143px">Phone:</span>
  <span class="t contact-value" style="left:624px;top:143px">(570) 413-CARE(2273)</span>
  <span class="t contact-label" style="left:482px;top:173px">Toll Free:</span>
  <span class="t contact-value" style="left:628px;top:173px">(855) 413-CARE</span>
  <span class="t contact-label" style="left:482px;top:203px">email 1:</span>
  <span class="t contact-value" style="left:624px;top:203px">Info@alderridgehh.org</span>
  <span class="t contact-label" style="left:482px;top:233px">email 2:</span>
  <span class="t contact-value" style="left:620px;top:233px">Careline@alderridgehh.org</span>
  <span class="t contact-label" style="left:482px;top:263px">address:</span>
  <span class="t contact-value" style="left:622px;top:263px;letter-spacing:2.4px">P.O. Box 287 Fernbrook, Pa 18990</span>

  <div class="logo-box" style="left:338px;top:405px;width:55px;height:73px"></div>
  <span class="t org-name" style="left:420px;top:402px">ALDER RIDGE</span>
  <span class="t org-tagline" style="left:455px;top:446px">Helping Harbor</span>
  <p class="mission">Is a Christ-centered organization dedicated to providing compassion and hope to homeless or near homes,<br>families and individual by meeting their basic and urgent need of food, clothing and shelter</p>

  <!-- back card content -->
  <p class="t verse" style="left:118px;top:690px">“I was hungry and you gave<br>me something to eat;</p>
  <p class="t verse" style="left:118px;top:793px">”I was thirsty and you gave<br>me something to drink;</p>
  <p class="t verse" style="left:118px;top:896px">”I was a stranger and you<br>invited me in.”</p>

  <span class="t org-name" style="left:573px;top:784px">ALDER RIDGE</span>
  <span class="t org-tagline" style="left:618px;top:836px">Helping Harbor</span>
  <div class="logo-box" style="left:908px;top:751px;width:105px;height:138px"></div>

  <span class="t foot-label" style="left:76px;top:1056px">Phone:</span>
  <span class="t foot-value" style="left:192px;top:1054px">(570) 413-CARE(2273)</span>
  <span class="t foot-label" style="left:76px;top:1086px">Toll Free<span style="color:var(--label)">:</span></span>
  <span class="t foot-value" style="left:192px;top:1084px">(855) 413-CARE</span>
  <span class="t foot-mail-label" style="left:550px;top:1056px">email 1:</span>
  <span class="t foot-mail" style="left:692px;top:1054px">Info@alderridgehh.org</span>
  <span class="t foot-mail-label" style="left:550px;top:1085px">email 2:</span>
  <span class="t foot-mail" style="left:692px;top:1083px">Careline@alderridgehh.org</span>
</main>
</body>
</html>
```